Thank You Card design for a federal credit union

I am looking to have a thank you card designed.
Specs:
Flat size of 9.5"x6.5" folds to final size of 4.75"x6.5", it will print full color on the front and back. Below, you will see their logo, which needs to print on the inside of the folded card. I also attached images of their current card. They would like to keep the blue color but are open to design on the front. This is a Federal Credit Union, so please make the design, modern and professional. Below is the text that needs to print below the logo on the inside of the card. The text and logo will print below the fold on the inside, leave the top portion (above the panel) white.
Inside text:
Our Members are the foundation of our Credit Union. We sincerely thank you for your loyalty, your business and the opportunity to serve you.
Target Market(s)
Clients of a federal credit union
Industry/Entity Type
Union
Requirements
Must have
- a simple, professional, and modern feel. "Thank You for your business" must be on the front section in some variation.
Should not have
- nothing flashy or too many colors. keep it simple

```html
<!DOCTYPE html>
<html lang="en">
<head>
<meta charset="utf-8">
<title>Thank You Card – Front and Inside</title>
<link rel="stylesheet" href="https://fonts.googleapis.com/css2?family=Raleway:wght@400&family=Great+Vibes&family=Crimson+Text:ital@0;1&family=Arimo:ital,wght@0,400;0,700;1,400&display=swap">
<style>
  :root {
    --navy: #0d1f6b;
    --navy-deep: #071450;
    --navy-light: #1c2e85;
    --paper: #f2f1ee;
    --blush: #f1e6e7;
    --silver: #e6e8ee;
    --ink-blue: #14247a;
    --card-stock: #f1efe6;
    --card-ink: #222222;
    --rule-green: #6aa84f;
    --label: #111111;
  }
  * { margin: 0; padding: 0; box-sizing: border-box; }
  html, body { width: 1200px; height: 906px; overflow: hidden; background: #ffffff; }
  .stage { position: relative; width: 1200px; height: 906px; }

  .panel { position: absolute; top: 43px; width: 535px; height: 795px; overflow: hidden; }
  .panel--front { left: 40px; }
  .panel--inside { left: 620px; }

  .panel-label {
    position: absolute; top: 848px; width: 535px; text-align: center;
    font-family: "Crimson Text", serif; font-size: 36px; color: var(--label);
  }
  .panel-label--front { left: 40px; }
  .panel-label--inside { left: 620px; }

  /* front */
  .front-blank { position: absolute; left: 0; top: 0; width: 100%; height: 397px; background: var(--paper); }
  .front-band {
    position: absolute; left: 0; top: 397px; width: 100%; height: 398px;
    background: radial-gradient(ellipse at 40% 55%, var(--navy-light) 0%, var(--navy) 45%, var(--navy-deep) 100%);
  }
  .front-kicker, .front-closer {
    position: absolute; left: 0; width: 100%; text-align: center;
    font-family: "Raleway", sans-serif; font-size: 18px; letter-spacing: 0.5em;
    color: #ffffff; padding-left: 0.5em;
  }
  .front-kicker { top: 468px; }
  .front-closer { top: 724px; }
  .front-rule { position: absolute; height: 1px; background: rgba(255,255,255,0.55); }
  .front-rule--top { left: 118px; width: 300px; top: 501px; }
  .front-rule--bottom { left: 118px; width: 300px; top: 709px; }
  .front-headline {
    position: absolute; left: 0; top: 548px; width: 100%; text-align: center;
    font-family: "Great Vibes", cursive; font-size: 118px; line-height: 1;
    color: var(--silver);
  }

  /* inside */
  .inside-top {
    position: absolute; left: 0; top: 0; width: 100%; height: 397px;
    background: linear-gradient(180deg, #0b1a5c 0%, var(--navy) 60%, #0e2275 100%);
  }
  .inside-bottom {
    position: absolute; left: 0; top: 397px; width: 100%; height: 398px;
    background: linear-gradient(180deg, var(--blush) 0%, #f4f0ef 45%, var(--blush) 100%);
  }
  .brand {
    position: absolute; left: 0; top: 420px; width: 100%;
    display: flex; justify-content: center; align-items: center; gap: 10px;
  }
  .brand-mark { width: 22px; height: 22px; background: var(--ink-blue); }
  .brand-name {
    font-family: "Crimson Text", serif; font-size: 24px; color: var(--ink-blue);
  }
  .brand-tagline {
    position: absolute; left: 0; top: 492px; width: 100%; text-align: center;
    font-family: "Arimo", sans-serif; font-style: italic; font-size: 10px; color: var(--ink-blue);
  }
  .inside-message {
    position: absolute; left: 0; top: 508px; width: 100%; text-align: center;
    font-family: "Crimson Text", serif; font-size: 19px; line-height: 29px; color: var(--ink-blue);
  }

  .business-card {
    position: absolute; left: 160px; top: 627px; width: 222px; height: 122px;
    background: var(--card-stock); font-family: "Arimo", sans-serif; color: var(--card-ink);
    box-shadow: 0 1px 2px rgba(0,0,0,0.2);
  }
  .bc-name { position: absolute; top: 8px; width: 100%; text-align: center; font-weight: 700; font-size: 12px; }
  .bc-title { position: absolute; top: 24px; width: 100%; text-align: center; font-size: 7px; }
  .bc-rule { position: absolute; left: 8px; right: 8px; top: 35px; height: 1px; background: var(--rule-green); }
  .bc-divider { position: absolute; left: 102px; top: 35px; width: 1px; height: 80px; background: var(--rule-green); }
  .bc-motto { position: absolute; left: 6px; top: 44px; width: 94px; text-align: center; font-family: "Crimson Text", serif; font-style: italic; font-size: 8px; }
  .bc-org { position: absolute; left: 6px; top: 62px; width: 94px; text-align: center; font-size: 9px; font-weight: 700; color: var(--ink-blue); line-height: 11px; }
  .bc-web { position: absolute; left: 6px; top: 104px; width: 94px; text-align: center; font-size: 6px; }
  .bc-contact { position: absolute; left: 106px; top: 46px; width: 112px; text-align: center; font-size: 7.5px; line-height: 10px; }
  .bc-contact p + p { margin-top: 6px; }
</style>
</head>
<body>
<main class="stage">

  <section class="panel panel--front">
    <div class="front-blank"></div>
    <div class="front-band" role="img" aria-label="Deep navy band scattered with falling confetti and curled streamers"></div>
    <p class="front-kicker">WE WOULD LIKE TO SAY</p>
    <div class="front-rule front-rule--top"></div>
    <h1 class="front-headline">Thank You</h1>
    <div class="front-rule front-rule--bottom"></div>
    <p class="front-closer">FOR YOUR BUSINESS</p>
  </section>
  <p class="panel-label panel-label--front">Front</p>

  <section class="panel panel--inside">
    <div class="inside-top" role="img" aria-label="Navy panel with purple confetti and curled streamers falling from the top edge"></div>
    <div class="inside-bottom" role="img" aria-label="Pale blush textured panel with faint white streamers"></div>

    <div class="brand">
      <span class="brand-mark"></span>
      <span class="brand-name">Harbor Point Federal Credit Union</span>
    </div>
    <p class="brand-tagline">People Over Profits</p>

    <p class="inside-message">
      Our Members are the foundation of our Credit Union.<br>
      We sincerely thank you for your loyalty,<br>
      your business and the opportunity to serve you.
    </p>

    <div class="business-card">
      <p class="bc-name">Dana Whitfield, CCUFC</p>
      <p class="bc-title">Marketing Manager</p>
      <div class="bc-rule"></div>
      <div class="bc-divider"></div>
      <p class="bc-motto">“People over Profits”</p>
      <p class="bc-org">Harbor Point<br>Federal Credit<br>Union</p>
      <p class="bc-web">www.harborpointfcu.org</p>
      <div class="bc-contact">
        <p>218 Larkin Street<br>Millbrook Falls, NY 12345</p>
        <p>(555) 201-4830<br>(555) 201-4899 fax</p>
        <p>dwhitfield@harborpointfcu.org</p>
      </div>
    </div>
  </section>
  <p class="panel-label panel-label--inside">Inside</p>

</main>
</body>
</html>
```